KTNW Unique Letterhead for Financial Services Business

I am looking for a letterhead design to match our branding colours. I do not want to see anything generic that could be created in word, I can do that myself, I am after something with a bit of designer flair. Once completed I will need files in a print ready format (including bleed area).

I have included our logo file and also our new business card design but get creative.

Industry/Entity Type

Financial Services

Font styles to use
Other font styles liked:
• raleway

Colors
00AB8E
00BBA5
67D7C9
C6EFE9
E9F9F6

Requirements
Must have
• Must be consisten with logo branding colours.
Should not have
• Anything generic that I could create myself in word

```html
<!DOCTYPE html>
<html lang="en">
<head>
<meta charset="utf-8">
<title>Kestrel Northway Letterhead</title>
<link rel="stylesheet" href="https://fonts.googleapis.com/css2?family=Raleway:wght@400;500&family=Source+Sans+3:wght@400;600&display=swap">
<style>
  :root {
    --backdrop: #e6e8e8;
    --paper: #ffffff;
    --teal-deep: #0f8a86;
    --teal: #1fa7a1;
    --teal-light: #4cc4bd;
    --brand-teal: #2a9fa3;
    --ink-heading: #1f5f86;
    --ink-body: #2d3040;
    --grey-block: #a6a8ab;
    --footer-bg: #f1f2f2;
    --footer-rule: #ffffff;
    --footer-text: #3a3d4a;
    --sig-line: #d8a35c;
  }
  * { margin: 0; padding: 0; box-sizing: border-box; }
  html, body { width: 900px; height: 1200px; overflow: hidden; }
  body {
    background: var(--backdrop);
    font-family: "Source Sans 3", "Myriad Pro", Arial, sans-serif;
    position: relative;
  }
  .letterhead {
    position: absolute;
    left: 50px; top: 35px;
    width: 800px; height: 1131px;
    background: var(--paper);
    box-shadow: 0 2px 10px rgba(0,0,0,.12);
    overflow: hidden;
  }
  .side-band {
    position: absolute;
    left: 0; top: 0;
    width: 153px; height: 100%;
    background: linear-gradient(180deg, var(--teal-light) 0%, var(--teal) 30%, var(--teal-deep) 55%, var(--teal) 78%, var(--teal-light) 100%);
  }
  .brand {
    position: absolute;
    left: 380px; top: 92px;
    width: 320px;
    display: flex;
    align-items: center;
    justify-content: center;
    gap: 10px;
  }
  .brand-square {
    width: 16px; height: 16px;
    background: var(--brand-teal);
  }
  .brand-name {
    font-family: "Raleway", sans-serif;
    font-weight: 500;
    font-size: 28px;
    letter-spacing: .5px;
    color: var(--brand-teal);
    text-transform: uppercase;
  }
  .corner-block {
    position: absolute;
    right: 0; top: 122px;
    width: 76px; height: 68px;
    background: var(--grey-block);
  }
  .sender {
    position: absolute;
    left: 224px; top: 296px;
    color: var(--ink-heading);
    font-weight: 600;
    font-size: 19px;
    line-height: 26px;
  }
  .letter-body {
    position: absolute;
    left: 224px; top: 382px;
    width: 540px;
    color: var(--ink-body);
    font-size: 14.6px;
    line-height: 25px;
  }
  .letter-body p + p { margin-top: 25px; }
  .signature {
    position: absolute;
    left: 224px; top: 790px;
    width: 150px; height: 60px;
  }
  .signature-mark {
    position: absolute;
    left: 0; top: 0;
    width: 150px; height: 52px;
    background: linear-gradient(90deg, rgba(45,48,64,.10), rgba(45,48,64,.04));
    border-radius: 26px;
  }
  .signature-rule {
    position: absolute;
    left: 0; bottom: 0;
    width: 150px; height: 2px;
    background: var(--sig-line);
  }
  .contact-bar {
    position: absolute;
    left: 201px; top: 1012px;
    width: 599px; height: 97px;
    background: var(--footer-bg);
    display: flex;
    color: var(--footer-text);
    font-size: 16px;
  }
  .contact-col {
    padding: 12px 0 0 30px;
    display: flex;
    flex-direction: column;
    gap: 3px;
  }
  .contact-col--direct { width: 284px; border-right: 3px solid var(--footer-rule); }
  .contact-col--address { padding-left: 22px; }
  .contact-item { display: flex; align-items: flex-start; gap: 10px; line-height: 22px; }
  .contact-item svg { flex: none; margin-top: 4px; }
  .address-lines { line-height: 20px; }
</style>
</head>
<body>
  <div class="letterhead">
    <div class="side-band" role="img" aria-label="Teal band with a soft floral damask pattern"></div>

    <div class="brand">
      <span class="brand-square"></span>
      <span class="brand-name">Kestrel Northway</span>
    </div>

    <div class="corner-block"></div>

    <div class="sender">
      <div>Lena Marsh</div>
      <div>Manager</div>
    </div>

    <div class="letter-body">
      <p>Lorem ipsum dolor sit amet, consectetuer adipiscing elit, sed diam nonummy nibh euismod tincidunt ut laoreet dolore magna aliquam erat volutpat. Ut wisi enim ad minim veniam, quis nostrud exerci tation ullamcorper suscipit lobortis nisl ut aliquip ex ea commodo consequat.</p>
      <p>Duis autem vel eum iriure dolor in hendrerit in vulputate velit esse molestie consequat, vel illum dolore eu feugiat nulla facilisis at vero zzril delenit augue duis dolore te feugait nulla facilisi.</p>
      <p>Lorem ipsum dolor sit amet, cons ectetuer adipiscing elit, sed diam nonummy nibh euismod tincidunt ut laoreet dolore magna aliquam erat volutpat. Ut wisi enim ad minim veniam, quis nostrud exerci tation ullamcorper suscipit lobortis nisl ut aliquip ex ea commodo consequat.</p>
    </div>

    <div class="signature">
      <div class="signature-mark" role="img" aria-label="Handwritten signature of the manager"></div>
      <div class="signature-rule"></div>
    </div>

    <div class="contact-bar">
      <div class="contact-col contact-col--direct">
        <div class="contact-item">
          <svg width="14" height="14" viewBox="0 0 14 14"><circle cx="7" cy="7" r="6.3" fill="none" stroke="#1fa7a1" stroke-width="1.2"/><path d="M4.6 3.8l1.2 1.3-.6.9c.5 1 1.2 1.7 2.2 2.2l.9-.6 1.3 1.2-.8 1c-2.6-.5-4.6-2.5-5.1-5.1z" fill="#1fa7a1"/></svg>
          <span>555 0148 202</span>
        </div>
        <div class="contact-item">
          <svg width="14" height="14" viewBox="0 0 14 14"><circle cx="7" cy="7" r="7" fill="#1fa7a1"/><rect x="3.5" y="4.8" width="7" height="4.6" fill="none" stroke="#fff" stroke-width="1"/><path d="M3.6 5l3.4 2.5L10.4 5" fill="none" stroke="#fff" stroke-width="1"/></svg>
          <span>hello@ktnw-mail.com</span>
        </div>
        <div class="contact-item">
          <svg width="14" height="14" viewBox="0 0 14 14"><circle cx="7" cy="7" r="7" fill="#1fa7a1"/><circle cx="7" cy="7" r="3.6" fill="none" stroke="#fff" stroke-width="1"/><path d="M3.4 7h7.2M7 3.4c-1.6 2.2-1.6 5 0 7.2M7 3.4c1.6 2.2 1.6 5 0 7.2" fill="none" stroke="#fff" stroke-width=".8"/></svg>
          <span>www.ktnw-example.com</span>
        </div>
      </div>
      <div class="contact-col contact-col--address">
        <div class="contact-item">
          <svg width="12" height="15" viewBox="0 0 12 15"><path d="M6 0.5a5 5 0 0 1 5 5c0 3.6-5 9-5 9s-5-5.4-5-9a5 5 0 0 1 5-5z" fill="#1fa7a1"/><circle cx="6" cy="5.5" r="1.8" fill="#fff"/></svg>
          <span class="address-lines">12 Harbour Row,<br>Tidewater Lane ,<br>Northfield-4410</span>
        </div>
      </div>
    </div>
  </div>
</body>
</html>
```